Postcard Mail Out - Wendell

We are a real estate company. We need a post card to mail out to potential clients to try and sale their land. We will attached a couple of post cards that we like but we do not want to copy them completely. We do need to put the Fair Dwelling Access and the Homebroker logos with a disclosure saying not intended to solicit currently listed properties. The image below is what we had started working on. We would like to include something about farm land, timber, maybe a pond, something along those lines. The PDF Files attached are a flyer that was mailed out by another company that we do not want to copy completely. Attached also will be our company's Logo.

Requirements
Must have
• We do need to put the Fair Dwelling Access and the Homebroker logos with a disclosure saying not intended to solicit currently listed properties.<br/><br/>At Cal Moreno Summit Realty, we are blessed to have one of the very best Rural Land Specialists available. Wendell has years of experience promoting and selling rural land properties. Wendell has earned the trust of many landowners, as he is so PASSIONATE in all regards to rural land, farms and ranches. He has made a wide range of landowners very happy throughout his years in Real Estate. Call him today and show him your property, and he will provide you with a free analysis and strategy to maximize the return on your property.
Nice to have
• A picture of Wendell has been added to use on the back of the post card with his phone and number. It would be nice to have a east Texas scenery picture behind him instead of an office.<br/><br/>Please include front and back of post card in your submission.
Should not have
• Should not have Ferris Dunmore's information on the postcard. That post card was just to show what we was wanting. The agent we want listed is Wendell Pruitt and his phone number is (555)413-2086.

```html
<!DOCTYPE html>
<html lang="en">
<head>
<meta charset="utf-8">
<title>Wendell Pruitt – Cal Moreno Summit Realty</title>
<link href="https://fonts.googleapis.com/css2?family=Archivo+Black&family=Roboto+Condensed:wght@700&family=Roboto:wght@400;500;700&display=swap" rel="stylesheet">
<style>
  :root {
    --paper: #ffffff;
    --ink: #111111;
    --muted: #444444;
    --blue-light: #3aa6d6;
    --blue-deep: #1a7bb0;
    --gold-light: #f7d84a;
    --gold-deep: #e6b81c;
    --shirt: #1b1f2e;
  }
  html, body {
    margin: 0;
    padding: 0;
    width: 1200px;
    height: 918px;
    overflow: hidden;
    background: var(--paper);
  }
  .postcard {
    position: relative;
    width: 1200px;
    height: 918px;
    overflow: hidden;
    background: var(--paper);
  }
  .scene-photo {
    position: absolute;
    inset: 0;
    width: 1200px;
    height: 918px;
  }
  .brand {
    position: absolute;
    left: 52px;
    top: 38px;
    display: flex;
    align-items: center;
    gap: 14px;
  }
  .brand-mark {
    width: 56px;
    height: 56px;
    border-radius: 50%;
    background: var(--paper);
  }
  .brand-name {
    font-family: "Roboto Condensed", sans-serif;
    font-weight: 700;
    font-size: 30px;
    line-height: 1.05;
    color: var(--paper);
    width: 260px;
  }
  .office-phone {
    position: absolute;
    left: 73px;
    top: 176px;
    font-family: "Roboto Condensed", sans-serif;
    font-weight: 700;
    font-size: 45px;
    color: var(--paper);
    letter-spacing: 0.5px;
  }
  .office-web {
    position: absolute;
    left: 120px;
    top: 228px;
    font-family: "Roboto", sans-serif;
    font-weight: 500;
    font-size: 26px;
    color: var(--paper);
  }
  .agent-story {
    position: absolute;
    left: 52px;
    top: 292px;
    width: 640px;
    margin: 0;
    font-family: "Roboto", sans-serif;
    font-weight: 500;
    font-size: 17px;
    line-height: 1.42;
    color: var(--paper);
    text-shadow: 0 1px 3px rgba(0, 0, 0, 0.55);
  }
  .agent-panel {
    position: absolute;
    left: 49px;
    top: 569px;
    width: 653px;
    height: 311px;
    border-radius: 20px;
    background: linear-gradient(135deg, var(--blue-light), var(--blue-deep));
  }
  .agent-name, .agent-phone {
    position: absolute;
    font-family: "Archivo Black", sans-serif;
    color: var(--paper);
    -webkit-text-stroke: 3px var(--ink);
    paint-order: stroke fill;
    text-shadow: 3px 4px 0 var(--ink);
    white-space: nowrap;
  }
  .agent-name { top: 68px; left: 29px; font-size: 72px; }
  .agent-phone { top: 170px; left: 24px; font-size: 75px; }
  .compliance {
    position: absolute;
    left: 49px;
    top: 886px;
    width: 700px;
    display: flex;
    align-items: center;
    gap: 16px;
    font-family: "Roboto", sans-serif;
    font-size: 12px;
    color: var(--muted);
    white-space: nowrap;
  }
  .badge {
    display: flex;
    align-items: center;
    gap: 5px;
    font-weight: 700;
    color: var(--ink);
  }
  .badge-square {
    width: 14px;
    height: 14px;
    background: var(--ink);
  }
  .agent-photo {
    position: absolute;
    left: 805px;
    top: 367px;
    width: 395px;
    height: 551px;
    border-radius: 160px 160px 0 0;
    background: linear-gradient(180deg, #c9a88f 0%, #8a6e5f 22%, var(--shirt) 38%, var(--shirt) 100%);
  }
</style>
</head>
<body>
<main class="postcard">
  <svg class="scene-photo" viewBox="0 0 1200 918" role="img" aria-label="Country home with stone chimney and porch, shade trees, landscaped garden and a pond">
    <defs>
      <linearGradient id="sceneTone" x1="0" y1="0" x2="0" y2="1">
        <stop offset="0" stop-color="#5f7f3a"/>
        <stop offset="0.35" stop-color="#7fa3bd"/>
        <stop offset="0.55" stop-color="#6b8a48"/>
        <stop offset="0.75" stop-color="#5f7e34"/>
        <stop offset="1" stop-color="#a89a80"/>
      </linearGradient>
      <linearGradient id="goldTone" x1="0" y1="0" x2="1" y2="1">
        <stop offset="0" stop-color="var(--gold-light)"/>
        <stop offset="1" stop-color="var(--gold-deep)"/>
      </linearGradient>
    </defs>
    <path d="M0 0 H1200 V640 H760 C600 640 300 660 0 664 Z" fill="url(#sceneTone)"/>
    <path d="M727 678 L1080 318 Q1095 304 1115 304 H1200 V918 H988 Z" fill="url(#goldTone)"/>
  </svg>

  <div class="brand">
    <span class="brand-mark"></span>
    <span class="brand-name">Cal Moreno Summit Realty</span>
  </div>
  <div class="office-phone">555-720-4418</div>
  <div class="office-web">1summitland.com</div>

  <p class="agent-story">At Cal Moreno Summit Realty, we are blessed to have one of the very best Rural Land Specialists available. Wendell has years of experience promoting and selling rural land properties – farm land, timber, ponds and ranches. He has earned the trust of many landowners, as he is so PASSIONATE in all regards to rural land. Call him today and show him your property, and he will provide you with a free analysis and strategy to maximize the return on your property.</p>

  <section class="agent-panel">
    <div class="agent-name">Wendell Pruitt</div>
    <div class="agent-phone">(555)413-2086</div>
  </section>

  <footer class="compliance">
    <span class="badge"><span class="badge-square"></span>Fair Dwelling Access</span>
    <span class="badge"><span class="badge-square"></span>Homebroker</span>
    <span class="disclosure">Not intended to solicit currently listed properties.</span>
  </footer>

  <div class="agent-photo" role="img" aria-label="Smiling agent in a dark shirt talking on a phone, East Texas scenery behind"></div>
</main>
</body>
</html>
```